looking for sleek business card to standout from the crowd!

We are a young biotechnology company looking to help you personalize your health through understanding your genetic make up. We need you help in making a clean but sleek business card design using our new logo. The goal? Any time we give our cards out, people say "nice card!" The feel we are going for is "modern-techy". We don't want to come across as an old, giant pharma company, but not trying to be a hipster either.

Target Market(s)

healthcare and biotechnology industry.

Industry/Entity Type

Biotechnology

Contact Information for Business Card

Info to include on the card will be NAME, TITLE, EMAIL, PHONE. The companies website (www.corvalinbio.com) should also be on the card some where. Would like the logo, when printed, to be raised.

Requirements
Must have
• The logo we have attached in the color it is in. Fonts for text should lean toward more professional/tech.
Nice to have
• Prefer white/light color background
Should not have
• cartoons, landscape backgrounds images.

```html
<!DOCTYPE html>
<html lang="en">
<head>
<meta charset="utf-8">
<title>Corvalin Business Card</title>
<link href="https://fonts.googleapis.com/css2?family=Open+Sans:wght@400;600;700&display=swap" rel="stylesheet">
<style>
  :root {
    --backdrop: #e9e7e4;
    --card-white: #ffffff;
    --brand-blue: #1572bb;
    --brand-blue-light: #2a86cc;
    --text-dark: #4a4a4a;
    --faint-circle: #f3f3f3;
  }
  html, body {
    margin: 0;
    padding: 0;
    width: 1200px;
    height: 1000px;
    overflow: hidden;
    background: var(--backdrop);
    font-family: "Open Sans", sans-serif;
  }
  .card {
    position: absolute;
    left: 266px;
    width: 666px;
    height: 397px;
    overflow: hidden;
    box-shadow: 0 4px 10px rgba(0,0,0,0.18);
  }
  .card-front { top: 74px; background: var(--card-white); }
  .card-back { top: 533px; background: var(--brand-blue); }

  .front-decor-circle {
    position: absolute;
    left: 333px;
    top: 126px;
    width: 302px;
    height: 302px;
    border-radius: 50%;
    background: var(--faint-circle);
  }
  .front-wordmark {
    position: absolute;
    right: 34px;
    top: 52px;
    display: flex;
    align-items: center;
    gap: 12px;
    font-weight: 700;
    font-size: 44px;
    letter-spacing: 1px;
    color: var(--brand-blue);
  }
  .wordmark-dot {
    width: 22px;
    height: 22px;
    border-radius: 50%;
    background: var(--brand-blue);
  }
  .holder-name {
    position: absolute;
    left: 33px;
    top: 56px;
    margin: 0;
    font-weight: 600;
    font-size: 21px;
    color: var(--brand-blue);
    letter-spacing: 0.3px;
  }
  .holder-title {
    position: absolute;
    left: 33px;
    top: 88px;
    margin: 0;
    font-size: 15.5px;
    color: var(--text-dark);
  }
  .address {
    position: absolute;
    left: 33px;
    top: 203px;
    margin: 0;
    font-style: normal;
    font-size: 16px;
    line-height: 26px;
    color: var(--text-dark);
  }
  .contact-list {
    position: absolute;
    left: 33px;
    top: 274px;
    margin: 0;
    padding: 0;
    list-style: none;
    font-size: 16px;
    line-height: 27px;
    color: var(--text-dark);
  }
  .contact-list li {
    display: flex;
    align-items: center;
    gap: 7px;
  }
  .contact-icon {
    width: 15px;
    height: 15px;
    fill: var(--brand-blue);
  }
  .back-wordmark {
    position: absolute;
    left: 0;
    right: 0;
    top: 158px;
    text-align: center;
    font-weight: 700;
    font-size: 68px;
    letter-spacing: 3px;
    color: var(--brand-blue-light);
  }
</style>
</head>
<body>
  <section class="card card-front">
    <div class="front-decor-circle" aria-hidden="true"></div>
    <div class="front-wordmark"><span>CORVALIN</span><span class="wordmark-dot"></span></div>
    <h1 class="holder-name">DANA WHITFORD</h1>
    <p class="holder-title">Managing Director/CEO</p>
    <address class="address">2180 North Alder Court<br>Hagerstown, MD 21740</address>
    <ul class="contact-list">
      <li>
        <svg class="contact-icon" viewBox="0 0 16 16"><path d="M2 6c0-2 3-3.5 6-3.5S14 4 14 6l-2.5 1-1-1.5h-5l-1 1.5zM4 8h8l1.5 5h-11z"/></svg>
        + 000 000 0000
      </li>
      <li>
        <svg class="contact-icon" viewBox="0 0 16 16"><path d="M1 4h14v9H1z" /><path d="M1 4l7 5 7-5" fill="none" stroke="#fff" stroke-width="1.3"/></svg>
        info@corvalinbio.com
      </li>
      <li>
        <svg class="contact-icon" viewBox="0 0 16 16"><circle cx="8" cy="8" r="7"/><path d="M1 8h14M8 1c-3 3-3 11 0 14M8 1c3 3 3 11 0 14" fill="none" stroke="#fff" stroke-width="1"/></svg>
        www.corvalinbio.com
      </li>
    </ul>
  </section>

  <section class="card card-back">
    <div class="back-wordmark">CORVALIN</div>
  </section>
</body>
</html>
```